Deactivated Coal-Fired Power Plant to be redeveloped into a Green Energy Campus.

Want a striking business card statement that introduces our concept project to provide economic and community recovery to a former rural coal community in western PA.
Essentially 12 project representatives that will lead both the demolition of an existing power plant and the redevelopment to a new Green energy site.
Business Card should reflect our effort.
We are open to ideas.

Target Market(s)

Energy and Power Generation industries

Industry/Entity Type

Power Generation and Data Centers

Contact Information for Business Card

Font styles to use
Sans Serif
Other font styles liked:
• Arial, Calibri

Requirements
Must have
• Multiple colors

```html
<!DOCTYPE html>
<html lang="en">
<head>
<meta charset="utf-8">
<title>Ridgeline Redevelopment – Business Card</title>
<link rel="stylesheet" href="https://fonts.googleapis.com/css2?family=Lato:wght@400;700&family=Roboto:wght@700&display=swap">
<style>
  :root {
    --backdrop: #9a9a9a;
    --card: #ffffff;
    --green: #12994a;
    --ink: #1a1a1a;
    --rule: #3a3a3a;
    --land-top: #c9d4dc;
    --land-mid: #6f8a5a;
    --land-low: #3f6a34;
  }
  * { margin: 0; padding: 0; box-sizing: border-box; }
  html, body { width: 1200px; height: 1000px; overflow: hidden; }
  body {
    background: var(--backdrop);
    font-family: "Lato", Arial, sans-serif;
    color: var(--ink);
    position: relative;
  }
  .card {
    position: absolute;
    left: 314px;
    width: 569px;
    height: 324px;
    background: var(--card);
    overflow: hidden;
  }
  .card--front { top: 133px; }
  .card--back { top: 545px; }

  .wordmark {
    position: absolute;
    display: flex;
    align-items: center;
    gap: 10px;
    font-family: "Lato", Arial, sans-serif;
    font-weight: 700;
    color: var(--ink);
    line-height: 1.05;
    letter-spacing: 0.04em;
  }
  .wordmark__dot {
    width: 34px; height: 34px;
    border-radius: 50%;
    background: var(--green);
    flex: none;
  }
  .wordmark__name { font-size: 21px; }
  .wordmark__name small { display: block; font-size: 11px; letter-spacing: 0.28em; margin-top: 4px; }
  .card--front .wordmark { right: 26px; top: 62px; }
  .card--back .wordmark { left: 26px; top: 84px; }

  .person__name {
    position: absolute; left: 26px; top: 166px;
    font-family: "Roboto", Arial, sans-serif;
    font-weight: 700; font-size: 20px;
    color: var(--green); letter-spacing: 0.01em;
  }
  .person__title {
    position: absolute; left: 26px; top: 191px;
    font-size: 13px;
  }
  .divider {
    position: absolute; left: 26px; right: 26px; top: 215px;
    border-top: 1px solid var(--rule);
  }
  .contact {
    position: absolute; left: 26px; top: 223px;
    list-style: none; font-size: 13.5px;
  }
  .contact__company { color: var(--green); margin-bottom: 3px; }
  .contact__item { display: flex; align-items: center; gap: 8px; height: 19.5px; }
  .contact__item svg { width: 10px; height: 11px; fill: var(--green); flex: none; }
  .website {
    position: absolute; right: 26px; top: 277px;
    font-size: 13px;
  }
  .website span { color: var(--green); }

  .back-art { position: absolute; inset: 0; }
</style>
</head>
<body>

<section class="card card--front">
  <div class="wordmark">
    <span class="wordmark__dot"></span>
    <span class="wordmark__name">RIDGELINE<small>REDEVELOPMENT</small></span>
  </div>

  <h1 class="person__name">DANIEL HARTWELL</h1>
  <p class="person__title">Chief Operating Officer</p>
  <div class="divider"></div>

  <ul class="contact">
    <li class="contact__company">Ridgeline Redevelopment LLC</li>
    <li class="contact__item">
      <svg viewBox="0 0 10 11"><path d="M2 0l2 2.5-1.2 1.3c.6 1.5 1.6 2.6 3 3.3L7 5.8l2.6 1.9-.8 2.4C4.5 10.5.3 6 0 1.7z"/></svg>
      412-555-0140
    </li>
    <li class="contact__item">
      <svg viewBox="0 0 10 11"><path d="M2 0h6v11H2zM3 1.2v7.2h4V1.2zM4.5 9.2h1v1h-1z" fill-rule="evenodd"/></svg>
      412-555-0199
    </li>
    <li class="contact__item">
      <svg viewBox="0 0 10 11"><path d="M0 2h10v1L5 6 0 3zM0 4.2l5 3 5-3V9H0z"/></svg>
      info@ridgelineredevelopment.com
    </li>
  </ul>

  <p class="website">www.<span>ridgelineredevelopment</span>.com</p>
</section>

<section class="card card--back">
  <svg class="back-art" viewBox="0 0 569 324" preserveAspectRatio="none">
    <defs>
      <linearGradient id="siteTones" x1="0" y1="0" x2="0" y2="1">
        <stop offset="0" stop-color="var(--land-top)"/>
        <stop offset="0.32" stop-color="#9fb0b5"/>
        <stop offset="0.45" stop-color="var(--land-mid)"/>
        <stop offset="1" stop-color="var(--land-low)"/>
      </linearGradient>
    </defs>
    <polygon points="388,0 557,0 557,324 85,324" fill="url(#siteTones)" role="img" aria-label="Aerial photograph of the power plant site with smokestacks among green hills"/>
    <polygon points="368,0 388,0 214,194 212,178" fill="var(--green)"/>
    <line x1="212" y1="179" x2="79" y2="324" stroke="var(--ink)" stroke-width="3"/>
    <rect x="557" y="0" width="12" height="324" fill="var(--green)"/>
  </svg>
  <div class="wordmark">
    <span class="wordmark__dot"></span>
    <span class="wordmark__name">RIDGELINE<small>REDEVELOPMENT</small></span>
  </div>
</section>

</body>
</html>
```